Now hiring billboard for roofing company

We would like to design/slogan for a "now hiring" billboard for a variety of positions in our roofing company.
We perform residential and commercial roofing.
We are looking to hire roofers, laborers, gutter installers, sheet metal workers, commercial drivers, commercial roofers, and residential and commercial service technicians.
Looking to attract both entry level and experienced roofers.
Roofing is a good industry to build a career, learn a trade, we provide training.

Opportunity to learn a trade and move from unskilled to skilled positions.
Use Brandell Roofing as a stepping stone in your career.

Brandell Roofing is a stable, growing company that has been providing roofing services in the Portland area for over 35 years. We have a great team of employees, many with over 10 years with the company.
In addition to roofing homes, our Residential Department also offers repair and cleaning services as well as gutter installation and repair.
In 2014 we added a dedicated Commercial Department that services commercial customers with roofing projects and service/repairs. In addition, they offer the Brandell topGuard maintenance program.
Mostly recently Brandell Roofing purchased Corvasse Sheet Metal (CSM) in 2016. CSM specializes in custom metal fabrication, continuous gutters and custom copper fabrication.

If you are looking for a job where you are appreciated
at a company that values honesty and respect,
come and join our team!
Whether you are experienced or just wanting to
learn, we are looking to add hard-working, reliable
go-getters to our team. We offer a flexible work
environment and in addition to full-time work offer
part-time and summer positions.
We are always looking to add great people to our
team. Some of the job/career options are:
• Residential Roofer
• Commercial Roofer
• Gutter Installer
• Service Technician
• Sheet Metal Fabricator/Installer
• Commercial Driver
• General Labor

Brandell Roofing offers competitive pay and an excellent benefits package.

Join our team today!

Target Market(s)

Job seekers

Font styles to use
Serif

Colors

Designer to choose colors to be used in the design.

Requirements
Must have
• Get across that we are hiring and have our contact info
• CCB #61834
• brandellwork.example
Nice to have
• Simple, easy to understand regardless of language literacy.
• Have a high proportion of Hispanic workers, maybe include Spanish.
• Spanish hiring phone number is 503-648-9013

```html
<!DOCTYPE html>
<html lang="en">
<head>
<meta charset="utf-8">
<title>Brandell Roofing – Now Hiring Billboard</title>
<link href="https://fonts.googleapis.com/css2?family=Ubuntu:wght@400;500;700&family=Roboto+Condensed:wght@400;500&display=swap" rel="stylesheet">
<style>
  :root {
    --navy: #3d4f7f;
    --navy-deep: #34446f;
    --orange: #f07f1e;
    --white: #ffffff;
    --rule: #9aa3b8;
    --swoosh: #d7dae2;
    --page: #eef0f3;
  }
  html, body {
    margin: 0;
    width: 912px;
    height: 1200px;
    overflow: hidden;
    background: var(--page);
  }
  .canvas {
    position: relative;
    width: 912px;
    height: 1200px;
  }
  .billboard {
    position: absolute;
    left: 20px;
    top: 416px;
    width: 1020px;
    height: 430px;
    transform: scale(0.855);
    transform-origin: 0 0;
    overflow: hidden;
    background: var(--white);
    font-family: "Ubuntu", sans-serif;
    box-shadow: 0 6px 18px rgba(0,0,0,.18);
  }
  .billboard-shapes {
    position: absolute;
    inset: 0;
  }
  .brand {
    position: absolute;
    left: 56px;
    top: 40px;
    font-size: 40px;
    font-weight: 700;
    color: var(--orange);
    letter-spacing: -0.5px;
    white-space: nowrap;
  }
  .license {
    position: absolute;
    left: 250px;
    top: 92px;
    font-family: "Roboto Condensed", sans-serif;
    font-size: 19px;
    font-weight: 500;
    color: var(--navy);
  }
  .offer-badge {
    position: absolute;
    left: 399px;
    top: 134px;
    width: 140px;
    height: 140px;
    text-align: center;
    color: var(--white);
  }
  .offer-title {
    margin-top: 40px;
    font-size: 18px;
    font-weight: 700;
    color: var(--orange);
  }
  .offer-text {
    margin-top: 2px;
    font-size: 10.5px;
    font-weight: 500;
    line-height: 13px;
  }
  .headline-tag {
    position: absolute;
    left: 812px;
    top: 20px;
    width: 182px;
    height: 31px;
    background: var(--navy);
    border-left: 5px solid var(--orange);
    box-sizing: border-box;
    color: var(--white);
    font-size: 25px;
    line-height: 31px;
    text-align: center;
    letter-spacing: 0.5px;
  }
  .headline {
    position: absolute;
    right: 20px;
    top: 50px;
    margin: 0;
    font-size: 49px;
    font-weight: 700;
    color: var(--orange);
    letter-spacing: 1.5px;
    white-space: nowrap;
  }
  .right-text {
    position: absolute;
    right: 20px;
    text-align: right;
    white-space: nowrap;
    color: var(--navy);
  }
  .lede { top: 106px; font-size: 11.5px; font-weight: 500; }
  .cta { top: 120px; font-size: 21px; font-weight: 500; }
  .cta .accent { color: var(--orange); font-weight: 700; }
  .intro { top: 164px; font-size: 12px; }
  .options-title { top: 180px; font-size: 15.5px; font-weight: 700; color: var(--orange); }
  .options-rule {
    position: absolute;
    left: 638px;
    right: 20px;
    top: 203px;
    height: 1px;
    background: var(--rule);
  }
  .job-list {
    position: absolute;
    top: 217px;
    margin: 0;
    padding: 0;
    list-style: none;
    text-align: right;
    font-size: 14.5px;
    font-weight: 500;
    line-height: 22px;
    color: var(--navy);
  }
  .job-list li::after {
    content: " •";
    color: var(--orange);
  }
  .job-list-primary { right: 318px; }
  .job-list-secondary { right: 24px; }
  .contact-bar {
    position: absolute;
    left: 470px;
    right: 16px;
    top: 386px;
    height: 34px;
    display: flex;
    align-items: center;
    justify-content: space-between;
    color: var(--white);
    white-space: nowrap;
  }
  .hiring-note {
    font-family: "Roboto Condensed", sans-serif;
    font-size: 10.5px;
    line-height: 12px;
  }
  .divider {
    width: 1px;
    height: 28px;
    background: var(--white);
  }
  .contact-item {
    display: flex;
    align-items: center;
    gap: 5px;
    font-family: "Roboto Condensed", sans-serif;
    font-size: 16px;
    font-weight: 500;
  }
  .contact-item .accent { color: var(--orange); font-weight: 400; }
  .web { font-family: "Ubuntu", sans-serif; font-size: 14px; }
</style>
</head>
<body>
<div class="canvas">
  <section class="billboard">
    <svg class="billboard-shapes" width="1020" height="430" viewBox="0 0 1020 430">
      <defs>
        <linearGradient id="photo-tones" x1="0" y1="0" x2="0.6" y2="1">
          <stop offset="0" stop-color="#9cc3e6"/>
          <stop offset="0.35" stop-color="#d9c9a4"/>
          <stop offset="0.65" stop-color="#b0603c"/>
          <stop offset="1" stop-color="#7a3b28"/>
        </linearGradient>
      </defs>
      <rect class="work-photo" x="0" y="0" width="560" height="430" fill="url(#photo-tones)" role="img" aria-label="Photo of two roofers working on timber roof battens above a brick house, with a ladder against the eaves"/>
      <path class="orange-arc" d="M388 0 L440 0 Q560 215 432 430 L398 430 Q528 215 388 0 Z" fill="var(--orange)"/>
      <path class="white-panel" d="M440 0 L1020 0 L1020 430 L432 430 Q560 215 440 0 Z" fill="var(--white)"/>
      <path class="swoosh" d="M400 404 Q460 336 700 326 Q900 318 1020 296 L1020 312 Q900 334 700 340 Q450 350 390 430 Z" fill="var(--swoosh)"/>
      <path class="contact-band" d="M380 430 Q440 352 700 344 Q900 338 1020 312 L1020 430 Z" fill="var(--navy)"/>
      <circle class="offer-circle" cx="469" cy="204" r="72" fill="var(--white)"/>
      <circle cx="469" cy="204" r="68" fill="var(--navy-deep)"/>
    </svg>

    <div class="brand">Brandell Roofing</div>
    <div class="license">CCB #61834</div>

    <div class="offer-badge">
      <div class="offer-title">WE OFFERING</div>
      <div class="offer-text">COMPETITIVE PAY AND<br>AN EXCELLENT<br>BENEFITS PACKAGE.</div>
    </div>

    <div class="headline-tag">IF YOU ARE</div>
    <h1 class="headline">LOOKING FOR A JOB</h1>
    <div class="right-text lede">WHERE YOU ARE APPRECIATED AT A COMPANY THAT VALUES HONESTY AND RESPECT,</div>
    <div class="right-text cta">COME AND <span class="accent">JOIN OUR TEAM!</span></div>
    <div class="right-text intro">WE ARE ALWAYS LOOKING TO ADD GREAT PEOPLE TO OUR TEAM</div>
    <div class="right-text options-title">SOME OF THE JOB/CAREER OPTIONS ARE:</div>
    <div class="options-rule"></div>

    <ul class="job-list job-list-primary">
      <li>Residential Roofer</li>
      <li>Commercial Roofer</li>
      <li>Gutter Installer</li>
      <li>General Labor</li>
    </ul>
    <ul class="job-list job-list-secondary">
      <li>Service Technician</li>
      <li>Sheet Metal Fabricator/Installer</li>
      <li>Commercial Driver</li>
      <li>Spanish/English Opportunities</li>
    </ul>

    <div class="contact-bar">
      <div class="hiring-note">GET ACROSS THAT WE ARE HIRING<br>AND HAVE OUR CONTACT INFO</div>
      <div class="divider"></div>
      <div class="contact-item phone">
        <svg width="15" height="15" viewBox="0 0 24 24" aria-hidden="true">
          <path d="M6.6 10.8a15.1 15.1 0 0 0 6.6 6.6l2.2-2.2a1 1 0 0 1 1-.25 11.4 11.4 0 0 0 3.6.57 1 1 0 0 1 1 1V20a1 1 0 0 1-1 1A17 17 0 0 1 3 4a1 1 0 0 1 1-1h3.5a1 1 0 0 1 1 1c0 1.25.2 2.45.57 3.57a1 1 0 0 1-.25 1Z" fill="var(--orange)"/>
        </svg>
        <span>503-648-9013 <span class="accent">(Spanish)</span></span>
      </div>
      <div class="divider"></div>
      <div class="contact-item web">
        <svg width="13" height="13" viewBox="0 0 24 24" aria-hidden="true">
          <circle cx="12" cy="12" r="10" fill="none" stroke="var(--orange)" stroke-width="2.4"/>
          <path d="M2 12h20M12 2c3 3 3 17 0 20M12 2c-3 3-3 17 0 20" fill="none" stroke="var(--orange)" stroke-width="1.6"/>
        </svg>
        <span>brandellwork.example</span>
      </div>
    </div>
  </section>
</div>
</body>
</html>
```